BRISK GUARD WEBSITE BANNER DESIGN OF AWESOME

Please take a look at the attached Banner. I want a redesign Idea. The requirements are below.

1)Must Use Website Background
2)Must Use Photo Provided
3)Must Include Button
4)Website the banner will be used on you can see the current at the bottom of the page: https://b.plomvarn.com

Target Market(s)

Anyone Seeking Security Guard Services

```html
<!DOCTYPE html>
<html lang="en">
<head>
<meta charset="utf-8">
<title>Brisk Guard – Website Banner</title>
<link rel="stylesheet" href="https://fonts.googleapis.com/css2?family=Lato:wght@400;700;900&display=swap">
<style>
  :root {
    --page-bg: #ffffff;
    --navy-deep: #1b3761;
    --navy-band: #1a4f80;
    --pill-navy: #1c3866;
    --gold: #f9b112;
    --white: #ffffff;
    --ink: #14243f;
    --photo-dark: #141f33;
    --photo-mid: #2c4670;
    --photo-light: #6f87b0;
  }
  * { margin: 0; padding: 0; box-sizing: border-box; }
  html, body {
    width: 1200px; height: 1200px; overflow: hidden;
    background: var(--page-bg);
    font-family: "Lato", Arial, sans-serif;
  }
  .banner {
    position: absolute; left: 0; top: 503px;
    width: 1200px; height: 194px;
    background: var(--navy-deep);
    overflow: hidden;
  }
  .banner-band { position: absolute; inset: 0; z-index: 0; }
  .guard-photo {
    position: absolute; left: 596px; top: 0; z-index: 1;
    width: 285px; height: 194px;
    background:
      radial-gradient(ellipse at 82% 14%, rgba(220,200,170,0.5), transparent 42%),
      linear-gradient(90deg, rgba(20,31,51,0) 0%, var(--photo-dark) 10%, var(--photo-dark) 42%, var(--photo-mid) 66%, var(--photo-light) 94%, rgba(111,135,176,0) 100%);
  }
  .brand-name {
    position: absolute; left: 790px; top: 20px; z-index: 3;
    width: 58px; text-align: center;
    color: var(--white); font-weight: 700; font-size: 10px;
    line-height: 1.2; letter-spacing: 0.5px;
  }
  .tagline {
    position: absolute; left: 364px; top: 48px; z-index: 2;
    width: 340px; height: 28px;
    background: var(--pill-navy);
    border-radius: 14px 0 0 14px;
    color: var(--white); font-weight: 700; font-size: 17px;
    line-height: 28px; padding-left: 12px; white-space: nowrap;
  }
  .headline {
    position: absolute; left: 362px; top: 10px; z-index: 3;
    font-weight: 700; font-size: 32px; line-height: 1;
    color: var(--white); letter-spacing: -0.2px; white-space: nowrap;
  }
  .headline .accent { color: var(--gold); }
  .feature {
    position: absolute; top: 85px; z-index: 3; width: 96px;
    display: flex; flex-direction: column; align-items: center;
  }
  .feature-portal { left: 339px; }
  .feature-dispatch { left: 418px; }
  .feature-contracts { left: 501px; }
  .feature svg { width: 35px; height: 40px; }
  .feature-label {
    margin-top: 6px; color: var(--white); font-size: 8.5px;
    font-weight: 700; white-space: nowrap;
  }
  .cta {
    position: absolute; left: 364px; top: 149px; z-index: 3;
    width: 116px; height: 25px; border-radius: 13px;
    background: var(--gold); color: var(--ink);
    font-weight: 900; font-size: 13.5px; line-height: 25px;
    text-align: center; white-space: nowrap;
  }
  .cta svg { width: 14px; height: 10px; vertical-align: -1px; }
</style>
</head>
<body>
  <section class="banner">
    <svg class="banner-band" width="1200" height="194" viewBox="0 0 1200 194" aria-hidden="true">
      <polygon points="56,0 1163,0 1126,96 19,96" fill="var(--navy-band)"/>
    </svg>

    <div class="guard-photo" role="img" aria-label="Photo of a security guard in a dark uniform shining a flashlight up a dim stairwell"></div>
    <span class="brand-name">BRISK GUARD</span>

    <p class="tagline">We take your security personal.</p>
    <h1 class="headline">GET <span class="accent">SECURED</span> TODAY</h1>

    <div class="feature feature-portal">
      <svg viewBox="0 0 36 41" aria-hidden="true">
        <path d="M18 1 L34 6 V22 C34 31 26 37 18 40 C10 37 2 31 2 22 V6 Z" fill="var(--gold)"/>
        <rect x="10" y="12" width="16" height="11" rx="1" fill="none" stroke="var(--ink)" stroke-width="1.2"/>
        <circle cx="18" cy="17.5" r="4" fill="none" stroke="var(--ink)" stroke-width="1"/>
        <path d="M14 26 H22 M18 23 V26" stroke="var(--ink)" stroke-width="1.2"/>
      </svg>
      <span class="feature-label">Client Portal</span>
    </div>
    <div class="feature feature-dispatch">
      <svg viewBox="0 0 36 41" aria-hidden="true">
        <path d="M18 1 L34 6 V22 C34 31 26 37 18 40 C10 37 2 31 2 22 V6 Z" fill="var(--gold)"/>
        <path d="M10 13 H21 V24 H10 Z M21 16 H25 L28 20 V24 H21" fill="none" stroke="var(--ink)" stroke-width="1.2"/>
        <circle cx="13" cy="25" r="2" fill="var(--gold)" stroke="var(--ink)" stroke-width="1.2"/>
        <circle cx="25" cy="25" r="2" fill="var(--gold)" stroke="var(--ink)" stroke-width="1.2"/>
        <path d="M6 16 H9 M5 19 H9" stroke="var(--ink)" stroke-width="1"/>
      </svg>
      <span class="feature-label">24x7 Dispatch</span>
    </div>
    <div class="feature feature-contracts">
      <svg viewBox="0 0 36 41" aria-hidden="true">
        <path d="M18 1 L34 6 V22 C34 31 26 37 18 40 C10 37 2 31 2 22 V6 Z" fill="var(--gold)"/>
        <rect x="11" y="9" width="14" height="17" fill="none" stroke="var(--ink)" stroke-width="1.2"/>
        <path d="M14 13 H22 M14 16 H22 M14 19 H20" stroke="var(--ink)" stroke-width="1"/>
        <path d="M9 27 L14 24 L18 27 L22 24 L27 27" fill="none" stroke="var(--ink)" stroke-width="1.2"/>
      </svg>
      <span class="feature-label">No Binding Contracts</span>
    </div>

    <div class="cta">GET STARTED
      <svg viewBox="0 0 14 10" aria-hidden="true"><path d="M1 1 L5 5 L1 9 M7 1 L11 5 L7 9" fill="none" stroke="var(--ink)" stroke-width="2.4"/></svg>
    </div>
  </section>
</body>
</html>
```